Double sided packaging design

Using our logo and its colors, please design a packaging design for our new Product Vitaloom.
The printable size is 140mm x 180mm, both sides
Vitaloom is a powdered formula of Cinnamon, turmeric, fennel, black pepper, 4 types of kelp & Seaweed, stevia and vanilla.
Its the flavor sensation that energizes your bodies Cells giving them all the food it needs to be healthy.

The old packaging we are moving away from as we have a new formula and we are also marketing for USA
It helps people with pain relief as its proven scientifically to reduce inflammation and other health benefits within the body such as cellular growth.

Please keep to the new colors of the Vitaloom Logo as supplied below

Target Market(s)

older women

Industry/Entity Type

Health Suplement Turmeric

Colors
59FF00
82FF00
B8FF75
E3FFCB
F4FFEA
FFC000
F8CF3A
FAE287
FDF2CF
FEFAEE

Requirements
Should not have
• not be too busy

```html
<!DOCTYPE html>
<html lang="en">
<head>
<meta charset="utf-8">
<title>Vitaloom Turmeric Chai Tea – Pouch Front and Back</title>
<link href="https://fonts.googleapis.com/css2?family=Alegreya+Sans:wght@700&family=Oswald:wght@300;400;500&family=Dancing+Script:wght@500&display=swap" rel="stylesheet">
<style>
  :root {
    --backdrop: #f2b922;
    --pouch: #f6f6f5;
    --ink: #2a2a2a;
    --ink-soft: #3d3d3d;
    --gold: #e7bf3a;
    --band: #f3cb52;
    --green: #2f9a3f;
    --green-head: #3aa04a;
    --white: #ffffff;
  }
  * { box-sizing: border-box; margin: 0; padding: 0; }
  html, body { width: 1200px; height: 1200px; overflow: hidden; }
  body { background: var(--backdrop); position: relative; font-family: "Oswald", sans-serif; color: var(--ink); }

  .panel { position: absolute; top: 228px; width: 556px; height: 744px; background: var(--pouch); overflow: hidden; }
  .panel--front { left: 30px; }
  .panel--back { left: 614px; }

  .band { position: absolute; left: 0; width: 100%; height: 96px; }
  .panel--front .band { top: 586px; }
  .panel--back .band { top: 590px; }

  .abs { position: absolute; }

  /* Front */
  .brand-name { font-family: "Oswald", sans-serif; font-weight: 300; color: var(--gold); letter-spacing: 2px; }
  .front-brand { left: 0; width: 100%; top: 216px; text-align: center; font-size: 46px; line-height: 1; }
  .product-title { left: 0; width: 100%; top: 280px; text-align: center; font-family: "Alegreya Sans", sans-serif; font-weight: 700; font-size: 40px; line-height: 37px; color: var(--ink); }
  .tagline { left: 0; width: 100%; top: 354px; text-align: center; font-size: 11px; line-height: 14px; letter-spacing: 2.5px; font-weight: 400; color: var(--ink-soft); }
  .front-art { left: 88px; top: 384px; width: 404px; height: 186px; border-radius: 0 0 200px 200px / 0 0 120px 120px; background: radial-gradient(ellipse at 55% 65%, #f1cf6c 0%, #cfe3a7 45%, #eef3e4 80%); }
  .band-headline { left: 0; width: 100%; top: 600px; text-align: center; font-size: 27px; line-height: 36px; font-weight: 300; color: var(--ink); }
  .band-script { left: 0; width: 100%; top: 638px; text-align: center; font-family: "Dancing Script", cursive; font-size: 22px; line-height: 28px; font-weight: 500; color: var(--ink); }
  .net-weight { left: 0; width: 100%; top: 694px; text-align: center; font-size: 20px; line-height: 26px; font-weight: 300; color: var(--ink-soft); }

  /* Back */
  .section-head { font-family: "Oswald", sans-serif; font-weight: 500; font-size: 11.5px; line-height: 16px; color: var(--green); }
  .copy { font-size: 11.2px; line-height: 15px; font-weight: 300; color: var(--ink); }
  .serving { left: 50px; top: 120px; width: 448px; }
  .ingredients { left: 51px; top: 190px; width: 448px; }

  .nutrition { left: 42px; top: 262px; width: 228px; table-layout: fixed; border-collapse: collapse; font-size: 9.4px; font-weight: 300; color: var(--ink); }
  .nutrition col.label { width: 80px; }
  .nutrition col.value { width: 74px; }
  .nutrition th, .nutrition td { border: 1px solid var(--ink-soft); height: 16px; padding: 0 4px; white-space: nowrap; }
  .nutrition .table-title { background: var(--green-head); color: var(--white); font-weight: 500; font-size: 10.5px; text-align: center; }
  .nutrition .serves { display: flex; justify-content: space-between; }
  .nutrition .col-head { font-size: 8px; line-height: 12px; text-align: center; font-weight: 400; height: 30px; }
  .nutrition td.num { text-align: center; }

  .back-art { left: 288px; top: 262px; width: 216px; height: 386px; border-radius: 40px 40px 110px 110px; background: linear-gradient(180deg, #f3f6ee 0%, #e3efcf 50%, #f3dc8d 100%); }

  .contact { left: 52px; top: 460px; font-size: 9.8px; line-height: 14px; font-weight: 300; }
  .back-brand { left: 146px; top: 476px; font-size: 24px; line-height: 1; }
  .maker { left: 53px; top: 506px; font-size: 9.8px; line-height: 14px; font-weight: 300; }
  .returns { left: 54px; top: 538px; font-size: 9.8px; line-height: 14px; font-weight: 300; }
  .code-box { left: 56px; top: 604px; width: 96px; height: 68px; background: var(--white); }
</style>
</head>
<body>

<section class="panel panel--front" aria-label="Pouch front">
  <svg class="band" viewBox="0 0 556 96" preserveAspectRatio="none" aria-hidden="true">
    <polygon fill="var(--band)" points="0,6 8,0 16,6 24,0 32,6 40,0 48,6 56,0 64,6 72,0 80,6 88,0 96,6 104,0 112,6 120,0 128,6 136,0 144,6 152,0 160,6 168,0 176,6 184,0 192,6 200,0 208,6 216,0 224,6 232,0 240,6 248,0 256,6 264,0 272,6 280,0 288,6 296,0 304,6 312,0 320,6 328,0 336,6 344,0 352,6 360,0 368,6 376,0 384,6 392,0 400,6 408,0 416,6 424,0 432,6 440,0 448,6 456,0 464,6 472,0 480,6 488,0 496,6 504,0 512,6 520,0 528,6 536,0 544,6 552,0 556,3 556,93 552,96 544,90 536,96 528,90 520,96 512,90 504,96 496,90 488,96 480,90 472,96 464,90 456,96 448,90 440,96 432,90 424,96 416,90 408,96 400,90 392,96 384,90 376,96 368,90 360,96 352,90 344,96 336,90 328,96 320,90 312,96 304,90 296,96 288,90 280,96 272,90 264,96 256,90 248,96 240,90 232,96 224,90 216,96 208,90 200,96 192,90 184,96 176,90 168,96 160,90 152,96 144,90 136,96 128,90 120,96 112,90 104,96 96,90 88,96 80,90 72,96 64,90 56,96 48,90 40,96 32,90 24,96 16,90 8,96 0,90"/>
  </svg>

  <div class="abs front-brand brand-name">Vitaloom</div>
  <h1 class="abs product-title">Turmeric<br>Chai Tea</h1>
  <p class="abs tagline">TASTE SENSATION</p>
  <div class="abs front-art" role="img" aria-label="Line drawing of a teacup on a saucer filled with turmeric root, cinnamon stick, green leaves, cardamom pods and peppercorns"></div>

  <p class="abs band-headline">Delicious spices in a unique powder</p>
  <p class="abs band-script">Australian made &amp; owned</p>
  <p class="abs net-weight">342 g NET</p>
</section>

<section class="panel panel--back" aria-label="Pouch back">
  <svg class="band" viewBox="0 0 556 96" preserveAspectRatio="none" aria-hidden="true">
    <polygon fill="var(--band)" points="0,6 8,0 16,6 24,0 32,6 40,0 48,6 56,0 64,6 72,0 80,6 88,0 96,6 104,0 112,6 120,0 128,6 136,0 144,6 152,0 160,6 168,0 176,6 184,0 192,6 200,0 208,6 216,0 224,6 232,0 240,6 248,0 256,6 264,0 272,6 280,0 288,6 296,0 304,6 312,0 320,6 328,0 336,6 344,0 352,6 360,0 368,6 376,0 384,6 392,0 400,6 408,0 416,6 424,0 432,6 440,0 448,6 456,0 464,6 472,0 480,6 488,0 496,6 504,0 512,6 520,0 528,6 536,0 544,6 552,0 556,3 556,93 552,96 544,90 536,96 528,90 520,96 512,90 504,96 496,90 488,96 480,90 472,96 464,90 456,96 448,90 440,96 432,90 424,96 416,90 408,96 400,90 392,96 384,90 376,96 368,90 360,96 352,90 344,96 336,90 328,96 320,90 312,96 304,90 296,96 288,90 280,96 272,90 264,96 256,90 248,96 240,90 232,96 224,90 216,96 208,90 200,96 192,90 184,96 176,90 168,96 160,90 152,96 144,90 136,96 128,90 120,96 112,90 104,96 96,90 88,96 80,90 72,96 64,90 56,96 48,90 40,96 32,90 24,96 16,90 8,96 0,90"/>
  </svg>

  <div class="abs serving">
    <h2 class="section-head">Serving Suggestion:</h2>
    <p class="copy">Prepare Vitaloom as you would your regular tea, just add to hot water, and let infuse for 1-2 minutes. The screw cap bottle included in the pouch is the recommended serve. If too gritty simply use blender to mill it down further, this gives even greater absorbing power.</p>
  </div>

  <div class="abs ingredients">
    <h2 class="section-head">Ingredients:</h2>
    <p class="copy">Turmeric, cinnamon, ground fennel, vanilla, calcium carbonate (E170), sodium bicarbonate (E500), ascorbic acid (E300), Kelp (0.16 g), black pepper, stevia, green tea, aniseed, caraway, ginger, liquorice, cloves, cardamom.</p>
  </div>

  <table class="abs nutrition">
    <colgroup><col class="label"><col class="value"><col class="value"></colgroup>
    <tr><th colspan="3" class="table-title">NUTRITIONAL INFORMATION</th></tr>
    <tr><td colspan="3"><div class="serves"><span>Servings per package: 31</span><span>Serving size: 10.90 g</span></div></td></tr>
    <tr><td></td><th class="col-head">Average Quantity<br>per Serving</th><th class="col-head">Average Quantity<br>per 100 g</th></tr>
    <tr><td>Energy</td><td class="num">126 kJ</td><td class="num">1160 kJ</td></tr>
    <tr><td>Protein</td><td class="num">0.6 g</td><td class="num">5.4 g</td></tr>
    <tr><td>Fat total</td><td class="num">0.9 g</td><td class="num">8.1 g</td></tr>
    <tr><td>Carbohydrates</td><td class="num">3.6 g</td><td class="num">32.8 g</td></tr>
    <tr><td>Sugars</td><td class="num">1.9 g</td><td class="num">17.6 g</td></tr>
    <tr><td>Sodium</td><td class="num">55 mg</td><td class="num">509 mg</td></tr>
  </table>

  <div class="abs back-art" role="img" aria-label="Hand lettering reading drink turmeric, taste sensation above a line drawing of a teacup with turmeric root, cinnamon stick and green leaves"></div>

  <p class="abs contact">Find us on:<br>info@vitaloom.com<br>www.vitaloom.com</p>
  <div class="abs back-brand brand-name">Vitaloom</div>
  <p class="abs maker">Manufactured in Australia for<br>Brightleaf Trading LLC</p>
  <p class="abs returns">Product returns<br>Suite 210 Brightleaf Trading LLC,<br>4420 Harbor View Rd Coral Bay, FL</p>
  <div class="abs code-box" aria-hidden="true"></div>
</section>

</body>
</html>
```